Trading Company needs a business card design, letter head design and email signature

We need a double-sided business card design, letter head design and an email signature. We have a logo design.

Possible Tag Lines:
• “Connecting Worlds, Building Excellence.”
• “Global Sourcing, Local Excellence.”
• “Bridging Borders, Building Quality.”
• “Worldwide Partnerships, Superior Goods.”
• “Where Quality Meets Affordability”

Services Offered:
Procurement
Fabrication
Distribution
Logistics
Import/Export

Requirements
Must have
• Nice quality double sided Business Card design, Letterhead design needs to be A4
Nice to have
• possible ideas on tag lines

```html
<!DOCTYPE html>
<html lang="en">
<head>
<meta charset="utf-8">
<title>Tradevia Stationery</title>
<link href="https://fonts.googleapis.com/css2?family=Open+Sans:wght@400;600;700&family=Lato:wght@400;700&family=Allura&display=swap" rel="stylesheet">
<style>
  :root{
    --red:#e5242b;
    --ink:#1f1f1f;
    --grey:#4a4b4d;
    --card:#1b1b1b;
    --card-mark:#2c2c2c;
    --paper:#ffffff;
    --backdrop:#e4e4e4;
    --light:#f2f2f2;
  }
  *{margin:0;padding:0;box-sizing:border-box}
  html,body{width:1200px;height:933px;overflow:hidden}
  body{background:var(--backdrop);position:relative;font-family:"Open Sans",sans-serif;color:var(--ink)}

  .letterhead{position:absolute;left:98px;top:53px;width:550px;height:777px;background:var(--paper)}
  .brand{position:absolute;display:flex;align-items:center;gap:8px;font-family:"Open Sans",sans-serif;font-weight:700;color:var(--red);letter-spacing:1px}
  .brand__square{display:block;background:var(--red)}
  .letterhead .brand{left:27px;top:70px;font-size:30px}
  .letterhead .brand__square{width:22px;height:22px}

  .contact{position:absolute;left:388px;top:28px;padding-left:18px;border-left:1.5px solid var(--red);font-family:"Lato",sans-serif;font-size:10.5px;line-height:12.3px;color:var(--ink)}
  .contact__row{display:flex;align-items:center;gap:4px}
  .contact__row svg{width:8px;height:8px;fill:var(--red);flex:none}
  .contact__address{margin-top:7px}

  .letter{position:absolute;left:28px;top:178px;width:494px;font-family:"Lato",sans-serif;font-size:11.2px;line-height:12.1px;color:var(--ink)}
  .letter__date{font-size:12px;margin-bottom:12px}
  .letter__recipient{font-size:11.5px;line-height:13px;margin-bottom:11px}
  .letter__greeting{font-size:14px;font-weight:700;margin:14px 0 13px}
  .letter p{text-align:justify;margin-bottom:12px}
  .letter__closing{margin-top:24px}
  .letter__signature{font-family:"Allura",cursive;font-size:28px;margin-top:52px}

  .card{position:absolute;left:756px;width:344px;height:196px;background:var(--card);border-radius:18px;color:#fff;font-family:"Open Sans",sans-serif}
  .card--front{top:378px}
  .card--back{top:601px}

  .card--front .brand{left:22px;top:117px;font-size:22px}
  .card--front .brand__square{width:16px;height:16px}
  .card__divider{position:absolute;left:197px;top:49px;width:1.5px;height:74px;background:var(--red)}
  .card__person{position:absolute;left:212px;top:45px;font-size:10px;line-height:12.2px}
  .card__name{font-size:14px;font-weight:700;color:var(--red);line-height:16px}
  .card__role{margin-bottom:6px}
  .card__person .contact__row svg{width:7px;height:7px}
  .card__address{margin-top:6px}
  .taglines{position:absolute;font-size:6.5px;line-height:9.8px;list-style:none}
  .taglines li::before{content:"• "}
  .taglines--left{left:13px;top:156px}
  .taglines--right{left:193px;top:164px}

  .card--back .brand{left:0;right:0;top:95px;justify-content:center;font-size:32px;color:var(--card-mark)}
  .card--back .brand__square{width:26px;height:26px;background:var(--card-mark)}
  .services__title{position:absolute;left:0;right:0;top:150px;text-align:center;color:var(--red);font-size:8px;font-weight:700}
  .services__list{position:absolute;left:0;right:0;top:166px;display:flex;justify-content:center;gap:5px;list-style:none;font-size:10px}
  .services__list li::before{content:"•";color:var(--red);margin-right:2px}
</style>
</head>
<body>

<section class="letterhead">
  <div class="brand"><span class="brand__square"></span>TRADEVIA</div>

  <div class="contact">
    <div class="contact__row"><svg viewBox="0 0 10 10"><path d="M1 3c0-1 1-2 4-2s4 1 4 2v1H7V3H3v1H1zM2 5h6l1 4H1z"/></svg>020 5190 4476</div>
    <div class="contact__row"><svg viewBox="0 0 10 10"><path d="M1 2h8v6H1zM1.8 2.8 5 5.3l3.2-2.5V3.6L5 6.1 1.8 3.6z" fill-rule="evenodd"/></svg>hello@tradevia-group.com</div>
    <div class="contact__row"><svg viewBox="0 0 10 10"><circle cx="5" cy="5" r="4.2"/></svg>www.tradevia-group.com</div>
    <div class="contact__address">Your address, City<br>State, Zip 1234</div>
  </div>

  <article class="letter">
    <div class="letter__date">January-03-2020</div>
    <div class="letter__recipient">Mr, Mark Ellison<br>President</div>
    <div class="letter__recipient">Northgate Holdings<br>123 Street Name, Suite# 10<br>City, State, 120023</div>
    <div class="letter__greeting">Dear Mr, Mark</div>
    <p>Lorem ipsum dolor sit amet, consectetur adipiscing elit, sed do eiusmod tempor incididunt ut labore et dolore magna aliqua. Ut enim ad minim veniam, quis nostrud exercitation ullamco laboris nisi ut aliquip ex ea commodo consequat. Duis aute irure dolor in reprehenderit in voluptate velit esse cillum dolore eu fugiat nulla pariatur.</p>
    <p>Lorem ipsum dolor sit amet, consectetur adipiscing elit, sed do eiusmod tempor incididunt ut labore et dolore magna aliqua. Ut enim ad minim veniam, quis nostrud exercitation ullamco laboris nisi ut aliquip ex ea commodo consequat. Duis aute irure dolor in reprehenderit in voluptate velit esse cillum dolore eu fugiat nulla pariatur.</p>
    <p>Lorem ipsum dolor sit amet, consectetur adipiscing elit, sed do eiusmod tempor incididunt ut labore et dolore magna aliqua. Ut enim ad minim veniam, quis nostrud exercitation ullamco laboris nisi ut aliquip ex ea commodo consequat.</p>
    <p>Excepteur sint occaecat cupidatat non proident, sunt in culpa qui officia deserunt mollit anim id est laborum. re et dolore magnam aliquam quaerat voluptatem.</p>
    <div class="letter__closing">Regards</div>
    <div class="letter__signature">Laura Pike</div>
  </article>
</section>

<section class="card card--front">
  <div class="brand"><span class="brand__square"></span>TRADEVIA</div>
  <div class="card__divider"></div>
  <div class="card__person">
    <div class="card__name">DANIEL REEVE</div>
    <div class="card__role">Managing Director</div>
    <div class="contact__row"><svg viewBox="0 0 10 10"><path d="M1 3c0-1 1-2 4-2s4 1 4 2v1H7V3H3v1H1zM2 5h6l1 4H1z"/></svg>555 248 019</div>
    <div class="contact__row"><svg viewBox="0 0 10 10"><path d="M1 2h8v6H1zM1.8 2.8 5 5.3l3.2-2.5V3.6L5 6.1 1.8 3.6z" fill-rule="evenodd"/></svg>daniel@tradevia-group.com</div>
    <div class="contact__row"><svg viewBox="0 0 10 10"><circle cx="5" cy="5" r="4.2"/></svg>www.tradevia.co</div>
    <div class="card__address">Your address, City<br>State, Zip 1234</div>
  </div>
  <ul class="taglines taglines--left">
    <li>“Connecting Worlds, Building Excellence.”</li>
    <li>“Global Sourcing, Local Excellence.”</li>
    <li>“Bridging Borders, Building Quality.”</li>
  </ul>
  <ul class="taglines taglines--right">
    <li>“Worldwide Partnerships, Superior Goods.”</li>
    <li>“Where Quality Meets Affordability”</li>
  </ul>
</section>

<section class="card card--back">
  <div class="brand"><span class="brand__square"></span>TRADEVIA</div>
  <div class="services__title">SERVICES OFFERED</div>
  <ul class="services__list">
    <li>Procurement</li>
    <li>Fabrication</li>
    <li>Distribution</li>
    <li>Logistics Import/Export</li>
  </ul>
</section>

</body>
</html>
```